Penny auction website for high end market

need a penny auction web design , requirement as below :-

- classy and noble, as i am only selli high end products
- 25 products for the main page , 5 products per row ( please see sample picture )
- top 5 products can be highlighted as those are limited edition products
- main page , products page, members page , faq and about us page
- matching logo with the name lotvo
- clean
- responsive for desktoop
-mobile version
Updates

i missed the mobile version, i should get the mobile version aswell, for desktop it should be responsive Added Wednesday, August 16, 2017

designer may use gold or silver color too as i am selling only high end products exclusively for members only, the layout can be different than the sample, it just a guide line for the sample, other better layout would be great to see and to have.

some idea how highend feel to me https://img.kravelshop.example/scr/51200/shining-gems-flash-cms-layout_52716-original.jpg

guys, please use this design https://www.pagewrenhub.example/flash-cms-layouts/52716.html as the base , i want it high class and up market, thanks

Target Market(s)

highend products buyer

Number of Pages Required

5+ page

Font styles to use
Serif
Sans Serif
Script
Other font styles liked:
• designer match it

Colors

Designer to choose colors to be used in the design.

Requirements
Must have
• source code, logos ( use lotvo for now, will change later when confirm ) , PSD
Nice to have
• more different type of designs would be great, designers can present they ideas other than my requirement

```html
<!DOCTYPE html>
<html lang="en">
<head>
<meta charset="utf-8">
<title>lotvo — Penny Auctions</title>
<link rel="stylesheet" href="https://fonts.googleapis.com/css2?family=Roboto:wght@300;400;500;700&display=swap">
<style>
:root{
  --gold:#b2a47b;
  --gold-dark:#9c8d62;
  --gold-light:#d8cfb3;
  --ink:#222222;
  --text:#3a3a3a;
  --muted:#8a8a8a;
  --line:#e4e4e4;
  --topbar:#0d0d0d;
  --footer:#2b2b2b;
  --footer-text:#b9b9b9;
  --cream:#f3f1ea;
  --white:#ffffff;
  --badge:#d62020;
}
*{box-sizing:border-box;margin:0;padding:0}
html,body{width:1200px;height:2432px;overflow:hidden}
body{font-family:'Roboto',Arial,sans-serif;color:var(--text);background:var(--white);position:relative}
.container{position:absolute;left:160px;width:878px}

/* top bar */
.topbar{position:absolute;top:0;left:0;width:1200px;height:31px;background:var(--topbar)}
.social{position:absolute;left:162px;top:5px;display:flex;gap:6px}
.social span{width:20px;height:20px;border-radius:50%;background:#4a4a4a;display:block}
.account-links{position:absolute;right:162px;top:9px;font-size:9.5px;color:var(--gold);letter-spacing:.3px;display:flex;gap:8px}
.account-links i{font-style:normal;color:#6a6a6a}

/* header */
.header{position:absolute;top:31px;left:0;width:1200px;height:73px;background:var(--white)}
.brand{position:absolute;left:160px;top:12px;display:flex;align-items:center;gap:9px}
.brand-circle{width:50px;height:50px;border-radius:50%;border:4px solid var(--gold);display:block}
.brand-name{font-size:30px;font-weight:400;color:#555}
.search{position:absolute;left:537px;top:19px;width:501px;height:38px;display:flex;border:1px solid #cfcfcf}
.search-field{flex:1;font-size:11px;color:#999;padding:12px 10px}
.search-btn{width:60px;background:var(--gold);display:flex;align-items:center;justify-content:center}

/* nav */
.nav{position:absolute;top:104px;left:0;width:1200px;height:48px;background:var(--gold)}
.nav-list{position:absolute;left:160px;top:0;display:flex;height:48px;list-style:none}
.nav-list li{font-size:11px;color:var(--white);padding:0 16px;line-height:48px;letter-spacing:.2px}
.nav-list li.active{background:var(--gold-dark)}
.cart{position:absolute;left:921px;top:0;width:117px;height:48px;background:var(--gold-dark);color:var(--white);font-size:11px;display:flex;align-items:center;justify-content:center;gap:8px}
.cart-icon{position:relative}
.cart-count{position:absolute;top:-9px;right:-8px;width:14px;height:14px;border-radius:50%;background:var(--badge);font-size:8px;line-height:14px;text-align:center;color:#fff}

/* hero */
.hero{position:absolute;top:152px;left:0;width:1200px;height:523px;overflow:hidden;background:#111}
.hero svg{position:absolute;left:0;top:0}
.hero-label{position:absolute;color:var(--white);font-size:24px;font-weight:300;letter-spacing:1px}
.hero-label.jewelry{left:76px;top:443px}
.hero-label.watches{left:334px;top:223px}
.hero-label.bags{left:675px;top:443px}
.hero-label.gadgets{left:929px;top:443px}
.hero-btn{position:absolute;left:360px;top:276px;width:146px;height:45px;border:2px solid var(--white);color:var(--white);font-size:13px;font-weight:500;letter-spacing:.5px;text-align:center;line-height:41px}

/* section headings */
.section-title{position:absolute;left:0;width:1200px;text-align:center;font-size:17px;font-weight:500;color:var(--ink);letter-spacing:.8px}
.divider{position:absolute;left:536px;width:128px;height:8px}

/* limited edition */
.limited{top:786px;display:flex;justify-content:space-between}
.limited-card{width:169px;height:236px;background:#f2f2f2;border:1px solid #dcdcdc;position:relative;text-align:center}
.limited-card::before{content:"";position:absolute;inset:5px;border:1px solid #cfc7ae}
.limited-photo{position:absolute;left:14px;top:14px;width:125px;height:130px}
.side-actions{position:absolute;right:9px;top:58px;display:flex;flex-direction:column;gap:8px}
.side-actions span{width:21px;height:21px;background:var(--gold);display:flex;align-items:center;justify-content:center}
.limited-title{position:absolute;left:0;right:0;top:164px;font-size:13px;font-weight:500;color:var(--ink)}
.limited-price{position:absolute;left:0;right:0;top:182px;font-size:11px;color:var(--ink)}
.limited-bid{position:absolute;left:59px;top:200px;width:52px;height:19px;background:var(--gold);color:#fff;font-size:8.5px;font-weight:500;line-height:19px}

/* product grid */
.grid{top:1134px;display:grid;grid-template-columns:repeat(5,169px);column-gap:8.25px;row-gap:11px}
.product{height:190px;border:1px solid var(--line);background:var(--white);position:relative}
.product-photo{position:absolute;left:0;top:0;width:167px;height:145px}
.product-bar{position:absolute;left:0;top:120px;width:167px;height:25px;display:flex;background:var(--gold)}
.product-bar .bid{flex:1;color:#fff;font-size:8px;font-weight:500;line-height:25px;padding-left:32px}
.product-bar .act{width:24px;border-left:1px solid rgba(255,255,255,.4);display:flex;align-items:center;justify-content:center}
.product-title{position:absolute;left:6px;top:154px;font-size:10px;font-weight:700;color:#444;letter-spacing:.5px}
.product-price{position:absolute;left:6px;top:169px;font-size:10px;font-weight:700;color:var(--gold)}

.tone-black{background:linear-gradient(160deg,#f4f4f4,#d9d9d9 60%,#2a2a2a 62%,#1a1a1a)}
.tone-silver{background:linear-gradient(150deg,#fafafa,#d8d4c6 55%,#b7ab85)}
.tone-coat{background:linear-gradient(180deg,#f2f2f2 0%,#47503a 30%,#3a4030 100%)}
.tone-chrome{background:linear-gradient(150deg,#fdfdfd,#e2e2e2 50%,#c9b98e)}
.tone-tan{background:linear-gradient(160deg,#c9a99a,#dcc38a 55%,#b79e64)}
.tone-watch{background:linear-gradient(160deg,#f5f5f5,#d2b9b5 50%,#8d7a6e)}
.tone-canvas{background:linear-gradient(150deg,#fafafa,#5d4a35 45%,#2b2220)}
.tone-rose{background:linear-gradient(160deg,#f3f3f3,#e3c5b2 50%,#c9a08a)}
.tone-red{background:linear-gradient(140deg,#f7f7f7 30%,#c0111b 50%,#8e0b12)}
.tone-tablet{background:linear-gradient(160deg,#f7f7f7,#3a3f4a 50%,#1c1f25)}
.tone-chain{background:linear-gradient(140deg,#f2f2f2,#b6794f 50%,#6c4228)}
.tone-turq{background:linear-gradient(160deg,#f2f2f2,#2b9a8e 50%,#a7793a)}
.tone-drop{background:linear-gradient(160deg,#f2f2f2,#b9b4a8 55%,#8f8a7d)}
.tone-brown{background:linear-gradient(160deg,#f2f2f2,#5b3324 55%,#3a1f16)}

/* newsletter */
.newsletter{position:absolute;top:1962px;left:0;width:1200px;height:198px;background:var(--cream)}
.newsletter-title{position:absolute;top:34px;left:0;width:1200px;text-align:center;font-size:17px;font-weight:500;color:var(--ink);letter-spacing:.5px}
.newsletter-sub{position:absolute;top:65px;left:0;width:1200px;text-align:center;font-size:11px;color:#555}
.newsletter-form{position:absolute;left:311px;top:117px;width:579px;height:39px;display:flex}
.newsletter-field{flex:1;background:#fff;font-size:11px;color:#999;padding:13px 10px}
.newsletter-btn{width:105px;background:var(--gold);color:#fff;font-size:10px;font-weight:500;display:flex;align-items:center;justify-content:center;gap:6px}

/* footer */
.footer{position:absolute;top:2160px;left:0;width:1200px;height:272px;background:var(--footer);color:var(--footer-text)}
.footer-brand{position:absolute;left:160px;top:30px;display:flex;align-items:center;gap:9px}
.footer-brand .brand-circle{border-color:#d9d9d9}
.footer-brand .brand-name{color:#d9d9d9}
.footer-about{position:absolute;left:160px;top:110px;width:200px;font-size:10.5px;line-height:16px}
.footer-col{position:absolute;top:48px}
.footer-col h4{font-size:11.5px;font-weight:500;color:#e6e6e6;letter-spacing:.4px}
.footer-col h4::after{content:"";display:block;width:24px;height:2px;background:var(--gold);margin-top:7px}
.footer-col ul{list-style:none;margin-top:26px}
.footer-col li{font-size:10.5px;height:24.7px;padding-left:27px;position:relative}
.footer-col li::before{content:"";position:absolute;left:0;top:5px;width:6px;height:6px;border-radius:50%;background:#d0d0d0}
.col-info{left:388px}
.col-account{left:611px}
.col-touch{left:835px}
.contact-line{display:flex;gap:14px;font-size:10.5px;line-height:16px;margin-bottom:8px}
.contact-line svg{flex:none;margin-top:2px}
.footer-rule{position:absolute;left:160px;top:219px;width:878px;height:1px;background:#444}
.copyright{position:absolute;left:162px;top:237px;font-size:10px}
.payments{position:absolute;right:162px;top:232px;display:flex;gap:9px}
.payments span{width:36px;height:22px;background:#d8d8d8;border-radius:2px;display:block}
</style>
</head>
<body>

<svg width="0" height="0" style="position:absolute" aria-hidden="true">
  <defs>
    <symbol id="i-heart" viewBox="0 0 16 16"><path d="M8 14 2.2 8.3A3.3 3.3 0 0 1 8 4a3.3 3.3 0 0 1 5.8 4.3Z" fill="#fff"/></symbol>
    <symbol id="i-eye" viewBox="0 0 16 16"><path d="M1 8c2-3.5 4.3-5 7-5s5 1.5 7 5c-2 3.5-4.3 5-7 5S3 11.5 1 8Z" fill="#fff"/><circle cx="8" cy="8" r="2.3" fill="var(--gold)"/></symbol>
    <symbol id="i-gavel" viewBox="0 0 16 16"><rect x="6" y="1" width="7" height="4" rx="1" transform="rotate(45 9.5 3)" fill="#fff"/><rect x="2" y="8" width="2.2" height="8" transform="rotate(-45 3 12)" fill="#fff"/></symbol>
  </defs>
</svg>

<div class="topbar">
  <div class="social" aria-label="Social links"><span></span><span></span><span></span><span></span></div>
  <div class="account-links">LOGIN <i>|</i> SIGN UP <i>|</i> MY ACCOUNT <i>|</i> WISHLIST</div>
</div>

<header class="header">
  <div class="brand"><span class="brand-circle"></span><span class="brand-name">lotvo</span></div>
  <div class="search">
    <div class="search-field">Search for product</div>
    <div class="search-btn"><svg width="16" height="16" viewBox="0 0 16 16"><circle cx="6.5" cy="6.5" r="4.5" fill="none" stroke="#fff" stroke-width="2"/><path d="M10 10l4.5 4.5" stroke="#fff" stroke-width="2.4"/></svg></div>
  </div>
</header>

<nav class="nav">
  <ul class="nav-list">
    <li class="active">HOME</li><li>ABOUT US</li><li>PRODUCTS</li><li>MEMBERS</li><li>FAQ'S</li><li>CONTACT US</li>
  </ul>
  <div class="cart">CART
    <span class="cart-icon"><svg width="16" height="15" viewBox="0 0 16 15"><path d="M2 5h12l-1 10H3Z" fill="#fff"/><path d="M5 6V4a3 3 0 0 1 6 0v2" fill="none" stroke="#fff" stroke-width="1.4"/></svg><span class="cart-count">2</span></span>
  </div>
</nav>

<section class="hero">
  <svg width="1200" height="523" viewBox="0 0 1200 523" role="img" aria-label="Four slanted photo panels: a woman wearing jewelry and rings, a close-up of a luxury wristwatch, a woman holding a brown leather handbag, and a dark textured smartphone back">
    <defs>
      <linearGradient id="g-jewel" x1="0" y1="0" x2="1" y2="1"><stop offset="0" stop-color="#6b5a52"/><stop offset=".5" stop-color="#b89282"/><stop offset="1" stop-color="#2a2321"/></linearGradient>
      <linearGradient id="g-watch" x1="0" y1="0" x2="1" y2="1"><stop offset="0" stop-color="#3a3a3a"/><stop offset=".5" stop-color="#1e1e1e"/><stop offset="1" stop-color="#0f0f0f"/></linearGradient>
      <linearGradient id="g-bag" x1="0" y1="0" x2="1" y2="1"><stop offset="0" stop-color="#8d8a78"/><stop offset=".45" stop-color="#d9c7ae"/><stop offset="1" stop-color="#5a2a1a"/></linearGradient>
      <linearGradient id="g-gadget" x1="0" y1="0" x2="1" y2="1"><stop offset="0" stop-color="#4a4a4a"/><stop offset=".6" stop-color="#1c1c1c"/><stop offset="1" stop-color="#0a0a0a"/></linearGradient>
    </defs>
    <polygon points="0,0 340,0 330,523 0,523" fill="url(#g-jewel)"/>
    <polygon points="340,0 640,0 560,523 330,523" fill="url(#g-watch)"/>
    <polygon points="640,0 957,0 860,523 560,523" fill="url(#g-bag)"/>
    <polygon points="957,0 1200,0 1200,523 860,523" fill="url(#g-gadget)"/>
    <rect x="330" y="0" width="330" height="523" fill="#000" opacity=".25"/>
  </svg>
  <div class="hero-label jewelry">JEWELRY</div>
  <div class="hero-label watches">PREMIUM WATCHES</div>
  <div class="hero-btn">GRAB IT NOW</div>
  <div class="hero-label bags">BAGS</div>
  <div class="hero-label gadgets">LUXURY GADGETS</div>
</section>

<h2 class="section-title" style="top:712px">LIMITED EDITION PRODUCTS</h2>
<svg class="divider" style="top:743px" viewBox="0 0 128 8"><path d="M0 4H52M76 4H128" stroke="var(--gold-light)" stroke-width="1"/><path d="M56 4q4-4 8 0t8 0" fill="none" stroke="var(--gold)" stroke-width="1.5"/></svg>

<div class="container limited">
  <article class="limited-card"><div class="limited-photo tone-chain" role="img" aria-label="Rose gold chain bracelet"></div>
    <div class="side-actions"><span><svg width="11" height="11"><use href="#i-heart"/></svg></span><span><svg width="11" height="11"><use href="#i-eye"/></svg></span><span><svg width="11" height="11"><use href="#i-gavel"/></svg></span></div>
    <div class="limited-title">PRODUCT TITLE</div><div class="limited-price">$1500.00</div><div class="limited-bid">BID NOW</div></article>
  <article class="limited-card"><div class="limited-photo tone-rose" role="img" aria-label="Rose gold leather handbag"></div>
    <div class="side-actions"><span><svg width="11" height="11"><use href="#i-heart"/></svg></span><span><svg width="11" height="11"><use href="#i-eye"/></svg></span><span><svg width="11" height="11"><use href="#i-gavel"/></svg></span></div>
    <div class="limited-title">PRODUCT TITLE</div><div class="limited-price">$1500.00</div><div class="limited-bid">BID NOW</div></article>
  <article class="limited-card"><div class="limited-photo tone-turq" role="img" aria-label="Turquoise drop earrings"></div>
    <div class="side-actions"><span><svg width="11" height="11"><use href="#i-heart"/></svg></span><span><svg width="11" height="11"><use href="#i-eye"/></svg></span><span><svg width="11" height="11"><use href="#i-gavel"/></svg></span></div>
    <div class="limited-title">PRODUCT TITLE</div><div class="limited-price">$1500.00</div><div class="limited-bid">BID NOW</div></article>
  <article class="limited-card"><div class="limited-photo tone-drop" role="img" aria-label="Silver diamond-shaped earrings"></div>
    <div class="side-actions"><span><svg width="11" height="11"><use href="#i-heart"/></svg></span><span><svg width="11" height="11"><use href="#i-eye"/></svg></span><span><svg width="11" height="11"><use href="#i-gavel"/></svg></span></div>
    <div class="limited-title">PRODUCT TITLE</div><div class="limited-price">$1500.00</div><div class="limited-bid">BID NOW</div></article>
  <article class="limited-card"><div class="limited-photo tone-brown" role="img" aria-label="Brown leather shoulder bag"></div>
    <div class="side-actions"><span><svg width="11" height="11"><use href="#i-heart"/></svg></span><span><svg width="11" height="11"><use href="#i-eye"/></svg></span><span><svg width="11" height="11"><use href="#i-gavel"/></svg></span></div>
    <div class="limited-title">PRODUCT TITLE</div><div class="limited-price">$1500.00</div><div class="limited-bid">BID NOW</div></article>
</div>

<h2 class="section-title" style="top:1063px">SHOP THAT NEW PRODUCTS</h2>
<svg class="divider" style="top:1094px" viewBox="0 0 128 8"><path d="M0 4H52M76 4H128" stroke="var(--gold-light)" stroke-width="1"/><path d="M56 4q4-4 8 0t8 0" fill="none" stroke="var(--gold)" stroke-width="1.5"/></svg>

<div class="container grid">
  <article class="product"><div class="product-photo tone-black" role="img" aria-label="Black nylon tote bag"></div><div class="product-bar"><span class="bid">BID NOW</span><span class="act"><svg width="10" height="10"><use href="#i-heart"/></svg></span><span class="act"><svg width="10" height="10"><use href="#i-eye"/></svg></span></div><div class="product-title">SAMPLE PRODUCT TITLE</div><div class="product-price">$1000.00</div></article>
  <article class="product"><div class="product-photo tone-silver" role="img" aria-label="Gold luxury slide phone"></div><div class="product-bar"><span class="bid">BID NOW</span><span class="act"><svg width="10" height="10"><use href="#i-heart"/></svg></span><span class="act"><svg width="10" height="10"><use href="#i-eye"/></svg></span></div><div class="product-title">SAMPLE PRODUCT TITLE</div><div class="product-price">$1000.00</div></article>
  <article class="product"><div class="product-photo tone-coat" role="img" aria-label="Dark green wool coat"></div><div class="product-bar"><span class="bid">BID NOW</span><span class="act"><svg width="10" height="10"><use href="#i-heart"/></svg></span><span class="act"><svg width="10" height="10"><use href="#i-eye"/></svg></span></div><div class="product-title">SAMPLE PRODUCT TITLE</div><div class="product-price">$1000.00</div></article>
  <article class="product"><div class="product-photo tone-chrome" role="img" aria-label="Silver music player with earphones"></div><div class="product-bar"><span class="bid">BID NOW</span><span class="act"><svg width="10" height="10"><use href="#i-heart"/></svg></span><span class="act"><svg width="10" height="10"><use href="#i-eye"/></svg></span></div><div class="product-title">SAMPLE PRODUCT TITLE</div><div class="product-price">$1000.00</div></article>
  <article class="product"><div class="product-photo tone-tan" role="img" aria-label="Beige leather handbag"></div><div class="product-bar"><span class="bid">BID NOW</span><span class="act"><svg width="10" height="10"><use href="#i-heart"/></svg></span><span class="act"><svg width="10" height="10"><use href="#i-eye"/></svg></span></div><div class="product-title">SAMPLE PRODUCT TITLE</div><div class="product-price">$1000.00</div></article>

  <article class="product"><div class="product-photo tone-watch" role="img" aria-label="Smartwatch with rose leather strap"></div><div class="product-bar"><span class="bid">BID NOW</span><span class="act"><svg width="10" height="10"><use href="#i-heart"/></svg></span><span class="act"><svg width="10" height="10"><use href="#i-eye"/></svg></span></div><div class="product-title">SAMPLE PRODUCT TITLE</div><div class="product-price">$1000.00</div></article>
  <article class="product"><div class="product-photo tone-canvas" role="img" aria-label="Monogram canvas travel bag"></div><div class="product-bar"><span class="bid">BID NOW</span><span class="act"><svg width="10" height="10"><use href="#i-heart"/></svg></span><span class="act"><svg width="10" height="10"><use href="#i-eye"/></svg></span></div><div class="product-title">SAMPLE PRODUCT TITLE</div><div class="product-price">$1000.00</div></article>
  <article class="product"><div class="product-photo tone-rose" role="img" aria-label="Rose gold leather handbag"></div><div class="product-bar"><span class="bid">BID NOW</span><span class="act"><svg width="10" height="10"><use href="#i-heart"/></svg></span><span class="act"><svg width="10" height="10"><use href="#i-eye"/></svg></span></div><div class="product-title">SAMPLE PRODUCT TITLE</div><div class="product-price">$1000.00</div></article>
  <article class="product"><div class="product-photo tone-red" role="img" aria-label="Red smartphone"></div><div class="product-bar"><span class="bid">BID NOW</span><span class="act"><svg width="10" height="10"><use href="#i-heart"/></svg></span><span class="act"><svg width="10" height="10"><use href="#i-eye"/></svg></span></div><div class="product-title">SAMPLE PRODUCT TITLE</div><div class="product-price">$1000.00</div></article>
  <article class="product"><div class="product-photo tone-tablet" role="img" aria-label="Tablet with keyboard cover"></div><div class="product-bar"><span class="bid">BID NOW</span><span class="act"><svg width="10" height="10"><use href="#i-heart"/></svg></span><span class="act"><svg width="10" height="10"><use href="#i-eye"/></svg></span></div><div class="product-title">SAMPLE PRODUCT TITLE</div><div class="product-price">$1000.00</div></article>

  <article class="product"><div class="product-photo tone-black" role="img" aria-label="Black nylon tote bag"></div><div class="product-bar"><span class="bid">BID NOW</span><span class="act"><svg width="10" height="10"><use href="#i-heart"/></svg></span><span class="act"><svg width="10" height="10"><use href="#i-eye"/></svg></span></div><div class="product-title">SAMPLE PRODUCT TITLE</div><div class="product-price">$1000.00</div></article>
  <article class="product"><div class="product-photo tone-silver" role="img" aria-label="Gold luxury slide phone"></div><div class="product-bar"><span class="bid">BID NOW</span><span class="act"><svg width="10" height="10"><use href="#i-heart"/></svg></span><span class="act"><svg width="10" height="10"><use href="#i-eye"/></svg></span></div><div class="product-title">SAMPLE PRODUCT TITLE</div><div class="product-price">$1000.00</div></article>
  <article class="product"><div class="product-photo tone-coat" role="img" aria-label="Dark green wool coat"></div><div class="product-bar"><span class="bid">BID NOW</span><span class="act"><svg width="10" height="10"><use href="#i-heart"/></svg></span><span class="act"><svg width="10" height="10"><use href="#i-eye"/></svg></span></div><div class="product-title">SAMPLE PRODUCT TITLE</div><div class="product-price">$1000.00</div></article>
  <article class="product"><div class="product-photo tone-chrome" role="img" aria-label="Silver music player with earphones"></div><div class="product-bar"><span class="bid">BID NOW</span><span class="act"><svg width="10" height="10"><use href="#i-heart"/></svg></span><span class="act"><svg width="10" height="10"><use href="#i-eye"/></svg></span></div><div class="product-title">SAMPLE PRODUCT TITLE</div><div class="product-price">$1000.00</div></article>
  <article class="product"><div class="product-photo tone-tan" role="img" aria-label="Beige leather handbag"></div><div class="product-bar"><span class="bid">BID NOW</span><span class="act"><svg width="10" height="10"><use href="#i-heart"/></svg></span><span class="act"><svg width="10" height="10"><use href="#i-eye"/></svg></span></div><div class="product-title">SAMPLE PRODUCT TITLE</div><div class="product-price">$1000.00</div></article>

  <article class="product"><div class="product-photo tone-watch" role="img" aria-label="Smartwatch with rose leather strap"></div><div class="product-bar"><span class="bid">BID NOW</span><span class="act"><svg width="10" height="10"><use href="#i-heart"/></svg></span><span class="act"><svg width="10" height="10"><use href="#i-eye"/></svg></span></div><div class="product-title">SAMPLE PRODUCT TITLE</div><div class="product-price">$1000.00</div></article>
  <article class="product"><div class="product-photo tone-canvas" role="img" aria-label="Monogram canvas travel bag"></div><div class="product-bar"><span class="bid">BID NOW</span><span class="act"><svg width="10" height="10"><use href="#i-heart"/></svg></span><span class="act"><svg width="10" height="10"><use href="#i-eye"/></svg></span></div><div class="product-title">SAMPLE PRODUCT TITLE</div><div class="product-price">$1000.00</div></article>
  <article class="product"><div class="product-photo tone-rose" role="img" aria-label="Rose gold leather handbag"></div><div class="product-bar"><span class="bid">BID NOW</span><span class="act"><svg width="10" height="10"><use href="#i-heart"/></svg></span><span class="act"><svg width="10" height="10"><use href="#i-eye"/></svg></span></div><div class="product-title">SAMPLE PRODUCT TITLE</div><div class="product-price">$1000.00</div></article>
  <article class="product"><div class="product-photo tone-red" role="img" aria-label="Red smartphone"></div><div class="product-bar"><span class="bid">BID NOW</span><span class="act"><svg width="10" height="10"><use href="#i-heart"/></svg></span><span class="act"><svg width="10" height="10"><use href="#i-eye"/></svg></span></div><div class="product-title">SAMPLE PRODUCT TITLE</div><div class="product-price">$1000.00</div></article>
  <article class="product"><div class="product-photo tone-tablet" role="img" aria-label="Tablet with keyboard cover"></div><div class="product-bar"><span class="bid">BID NOW</span><span class="act"><svg width="10" height="10"><use href="#i-heart"/></svg></span><span class="act"><svg width="10" height="10"><use href="#i-eye"/></svg></span></div><div class="product-title">SAMPLE PRODUCT TITLE</div><div class="product-price">$1000.00</div></article>
</div>

<section class="newsletter">
  <h2 class="newsletter-title">SUBSCRIBE TO NEWSLETTER</h2>
  <p class="newsletter-sub">Contrary to popular belief, Lorem Ipsum is not simply random text</p>
  <div class="newsletter-form">
    <div class="newsletter-field">Enter your email</div>
    <div class="newsletter-btn"><svg width="11" height="9" viewBox="0 0 11 9"><rect x=".5" y=".5" width="10" height="8" fill="none" stroke="#fff"/><path d="M.5 .5l5 4 5-4" fill="none" stroke="#fff"/></svg>SUBSCRIBE</div>
  </div>
</section>

<footer class="footer">
  <div class="footer-brand"><span class="brand-circle"></span><span class="brand-name">lotvo</span></div>
  <p class="footer-about">There are many variations of passages of Lorem Ipsum available, but the majority have suffered alteration in some form, by injected humour, or randomised words which don't look even slightly believable.</p>

  <div class="footer-col col-info"><h4>INFORMATION</h4>
    <ul><li>My Account</li><li>Order History</li><li>Contact Us</li><li>Terms &amp; Condition</li></ul></div>
  <div class="footer-col col-account"><h4>MY ACCOUNT</h4>
    <ul><li>Privacy Policy</li><li>Delivery Information</li><li>Manufacturers</li><li>Site Map</li></ul></div>
  <div class="footer-col col-touch"><h4>GET IN TOUCH</h4>
    <div style="margin-top:26px">
      <div class="contact-line"><svg width="9" height="12" viewBox="0 0 9 12"><path d="M4.5 12S0 6.8 0 4.5a4.5 4.5 0 0 1 9 0C9 6.8 4.5 12 4.5 12Z" fill="#d0d0d0"/><circle cx="4.5" cy="4.5" r="1.6" fill="var(--footer)"/></svg><span>There are many variations of<br>passages of Lorem Ipsum available</span></div>
      <div class="contact-line"><svg width="11" height="11" viewBox="0 0 11 11"><path d="M2 0l2 3-1.2 1.3a7 7 0 0 0 3.9 3.9L8 7l3 2-1.5 2C4.5 11 0 6.5 0 1.5Z" fill="#d0d0d0"/></svg><span>(+1)555-014-2280</span></div>
      <div class="contact-line"><svg width="11" height="9" viewBox="0 0 11 9"><rect x=".5" y=".5" width="10" height="8" fill="none" stroke="#d0d0d0"/><path d="M.5 .5l5 4 5-4" fill="none" stroke="#d0d0d0"/></svg><span>info@lotvo-auctions.example</span></div>
    </div>
  </div>

  <div class="footer-rule"></div>
  <p class="copyright">Copyright © 2017 lotvo. All rights reserved.</p>
  <div class="payments" aria-label="Accepted payment methods"><span></span><span></span><span></span><span></span><span></span></div>
</footer>

</body>
</html>
```